Farhan Jewellers Stationary Contest

Pakistan’s largest Jewellery, Diamond and luxury watches store requires professional stationery. We have a long list of are trusted clients since 1959, our third generation has successfully maintained and sustained the legacy and excellence in the sector.

We require stationery template as part of this contest. The stationery can be double sided.

We prefer a design that makes use of some of the premium business stationery printing options, such as foil stamping, embossing/debossing, painted edges, spot UV etc (doesn't have to use all these options, only what you feel works, but we are looking for a design that stands out and is memorable and these nice touches have that effect.)

We want an eye catching, innovative, high end professional looking stationery for an out of box design that blends well with our new logo (attached). We want the design to be an out of box solution, you may use any element to compliment the logo. You may consider incorporating watermark etc, highlighting our products (Gold and Diamond Jewellery in addition to Luxury watches)

Company details are as follows;

Company name: Farhan Jewellers
Contact Person: Tariq Naveed
Designation: Business Development Consultant
Mobile: +92 333 815 6042
Email: tariqnaveed@mailvora.com
Website: www.farhanjewellers-pk.net

Target Market(s)

Matrimonial, Elite & Businesses class, Upmarket

Font styles to use
Other font styles liked:
• Designers choice

Colors

Designer to choose colors to be used in the design.

Requirements
Must have
• Look and feel: Upmarket, innovative, Modern, Professional, graceful, Elegant, designer stuff.
Nice to have
• Unique design

```html
<!DOCTYPE html>
<html lang="en">
<head>
<meta charset="utf-8">
<title>Farhan Jewellers – Stationery</title>
<link href="https://fonts.googleapis.com/css2?family=Montserrat:wght@600&family=Open+Sans:wght@400;600&family=Lora&family=Great+Vibes&display=swap" rel="stylesheet">
<style>
  :root{
    --backdrop:#2e2e2e;
    --paper:#ffffff;
    --gold:#d6a21f;
    --gold-deep:#c8951a;
    --gold-card:#d7a629;
    --ink:#1c1c1c;
    --muted:#555555;
    --watermark:rgba(214,162,31,0.16);
  }
  *{margin:0;padding:0;box-sizing:border-box}
  html,body{width:1200px;height:1200px;overflow:hidden;background:var(--backdrop)}
  body{position:relative;font-family:"Open Sans",sans-serif;color:var(--ink)}
  .sheet{position:absolute;background:var(--paper);overflow:hidden;box-shadow:0 8px 24px rgba(0,0,0,.35)}
  .ornament{position:absolute;border-radius:50%}
  .brand{display:flex;align-items:center;gap:8px;font-family:"Montserrat",sans-serif;font-weight:600;letter-spacing:.06em;text-transform:uppercase;color:var(--gold);white-space:nowrap}
  .brand-dot{border-radius:50%;background:var(--gold);flex:none}

  /* Business card front */
  .card-front{left:40px;top:176px;width:480px;height:274px}
  .card-front .ornament{right:-40px;top:-50px;width:230px;height:230px;background:radial-gradient(circle,var(--watermark) 0%,rgba(214,162,31,.1) 55%,transparent 72%)}
  .card-front .brand{position:absolute;left:34px;top:40px;font-size:15px}
  .card-front .brand-dot{width:12px;height:12px}
  .card-name{position:absolute;left:34px;top:104px;font-family:"Great Vibes",cursive;font-size:34px;color:var(--gold)}
  .card-role{position:absolute;left:36px;top:148px;font-size:11px;color:var(--muted)}
  .card-contacts{position:absolute;left:36px;top:182px;font-size:11px;line-height:19px;list-style:none}
  .card-contacts b{display:inline-block;width:18px;color:var(--gold);font-weight:600}

  /* Business card back */
  .card-back{left:40px;top:474px;width:480px;height:274px;background:var(--gold-card)}
  .card-back .ornament{right:-50px;top:-60px;width:250px;height:250px;background:radial-gradient(circle,rgba(150,100,10,.35) 0%,rgba(150,100,10,.18) 55%,transparent 72%)}
  .card-back .brand{position:absolute;left:50%;top:50%;transform:translate(-50%,-50%);font-size:24px;color:var(--ink)}
  .card-back .brand-dot{width:18px;height:18px;background:var(--ink)}

  /* Envelope */
  .envelope{left:40px;top:772px;width:480px;height:229px}
  .envelope .ornament{right:-50px;top:-30px;width:260px;height:260px;background:radial-gradient(circle,var(--watermark) 0%,rgba(214,162,31,.08) 58%,transparent 72%)}
  .envelope .brand{position:absolute;left:30px;top:100px;font-size:15px}
  .envelope .brand-dot{width:12px;height:12px}
  .envelope address{position:absolute;left:30px;top:134px;font-style:normal;font-family:"Lora",serif;font-size:13px;line-height:19px;color:var(--ink)}

  /* Letterhead */
  .letterhead{left:560px;top:176px;width:600px;height:848px}
  .letterhead .ornament{right:-110px;bottom:40px;width:480px;height:480px;background:radial-gradient(circle,var(--watermark) 0%,rgba(214,162,31,.09) 55%,transparent 72%)}
  .letterhead .brand{position:absolute;left:48px;top:92px;font-size:17px}
  .letterhead .brand-dot{width:14px;height:14px}
  .lh-contacts{position:absolute;right:48px;top:48px;list-style:none;font-size:10px;line-height:15px;color:var(--ink)}
  .lh-contacts li{display:flex;align-items:center;gap:6px}
  .lh-contacts .icon{width:8px;height:8px;background:var(--gold);border-radius:2px}
  .lh-contacts .plain{padding-left:14px}
  .recipient{position:absolute;left:48px;top:178px;font-size:10px;line-height:20px}
  .letter-body{position:absolute;left:48px;top:260px;width:500px;font-size:10px;line-height:17px;color:#333}
  .letter-body p{margin-bottom:16px}
  .letter-body ul{margin:0 0 16px 16px}
  .lh-footer{position:absolute;left:48px;right:40px;bottom:34px;font-size:10px;color:var(--ink);white-space:nowrap}
  .lh-footer b{color:var(--gold);font-weight:600}
</style>
</head>
<body>

<section class="sheet card-front">
  <div class="ornament" role="img" aria-label="Faint gold ornamental watermark"></div>
  <div class="brand"><span class="brand-dot"></span>Farhan Jewellers</div>
  <div class="card-name">Tariq Naveed</div>
  <div class="card-role">Business Development Consultant</div>
  <ul class="card-contacts">
    <li><b>M.</b>+92 333 815 6042</li>
    <li><b>E.</b>tariqnaveed@mailvora.com</li>
    <li><b>W.</b>www.farhanjewellers-pk.net</li>
  </ul>
</section>

<section class="sheet card-back">
  <div class="ornament" role="img" aria-label="Tone-on-tone gold ornamental pattern"></div>
  <div class="brand"><span class="brand-dot"></span>Farhan Jewellers</div>
</section>

<section class="sheet envelope">
  <div class="ornament" role="img" aria-label="Faint gold ornamental watermark"></div>
  <div class="brand"><span class="brand-dot"></span>Farhan Jewellers</div>
  <address>48 Garden Arcade<br>Gulberg Plaza, Lahore - Pakistan</address>
</section>

<section class="sheet letterhead">
  <div class="ornament" role="img" aria-label="Large faint gold ornamental watermark"></div>
  <ul class="lh-contacts">
    <li><span class="icon"></span>/ farhanjewellerspk</li>
    <li><span class="icon"></span>@farhanjewellers</li>
    <li><span class="icon"></span>farhanjewellers</li>
    <li class="plain">48 Garden Arcade</li>
    <li class="plain">Gulberg Plaza, Lahore - Pakistan</li>
  </ul>
  <div class="brand"><span class="brand-dot"></span>Farhan Jewellers</div>
  <div class="recipient">To<br>The,<br>Director</div>
  <div class="letter-body">
    <p>Lorem ipsum dolor sit amet, consectetur adipiscing elit. Sed at ante. Mauris eleifend, quam a vulputate dictum, massa quam dapibus leo, eget vulputate orci purus ut lorem. In fringilla mi in ligula. Pellentesque aliquam quam vel dolor. Nunc adipiscing. Sed quamodio, tempus ac, aliquam molestie varius ac, tellus. Vestibulum ut nulla aliquam risus rutrum interdum. Pellentesque lorem.</p>
    <ul>
      <li>Curabitur sit amet erat quis risus feugiat viverra. Pellentesque augue justo, sagittis etc.</li>
      <li>Nunc nec libero. In cursus dictum risus. Etiam tristique nisl a nulla. Ut a orci.</li>
      <li>Vestibulum ante ipsum primis in faucibus orci luctus et ultrices posuere cubilia Curae.</li>
    </ul>
    <p>Sed consequat, tellus eu volutpat varius, justo orci elementum dolor, sed imperdiet ante, malesuada quis, tempus ac, placerat sit amet, elit. Curabitur sit amet erat quis risus feugiat viverra. Pellentesque augue justo, sagittis et, lacinia at, venenatis dictum risus. Etiam tristique nisl a nulla. Ut a orci. Curabitur dolor, egestas Nulla facilisi. Nunc volutpat. Vestibulum ante ipsum primis in faucibus Curae; Ut sit amet orci vel mauris blandit vehicula. Nullam quis enim. Integer.</p>
  </div>
  <div class="lh-footer"><b>T.</b> +92 42 35461180-2 | <b>F.</b> +92 42 35462715 | <b>E.</b> info@farhanjewellers-pk.net | <b>W.</b> www.farhanjewellers-pk.net</div>
</section>

</body>
</html>
```